Velmira Home Page

I want to design a new home page using the look of two pages that I like.
http://us.dorazzi.com/
http://www.monvelle.us/?cm_mmc=searvo-_-EG_BR_Monvelle_Exact_CAR_D-_-Search-_-monvellehttp://us.dorazzi.com/
I like the framing of the dorazzi site and the drop down feel of the monvelle site. I will provide a new logo later today but for now can use what is already on my home page. The pictures in the middle of the page will rotate but I like the fonts and framing from Dorazzi.
My current site is www.velmira.com and I had a designer do a file which came close but missed the mark attached. This upscale and elegant
I liek the top log but would want the glass tilted to look liek the rest of the letters and in a grey or silver elegant color.
High end individuals andn corporations

```html
<!DOCTYPE html>
<html lang="en">
<head>
<meta charset="utf-8">
<title>Velmira — Travel</title>
<link rel="stylesheet" href="https://fonts.googleapis.com/css2?family=Old+Standard+TT:wght@400;700&display=swap">
<style>
  :root {
    --ink: #ffffff;
    --ink-soft: #d9dee2;
    --ink-muted: #b9c0c6;
    --night: #000000;
    --band: rgba(10, 14, 18, 0.72);
    --header-shade: rgba(8, 12, 16, 0.55);
    --rule: rgba(255, 255, 255, 0.35);
    --sky-light: #d8e2e4;
    --sky-mid: #3f7c86;
    --sky-deep: #153c48;
    --sky-edge: #061820;
  }
  * { margin: 0; padding: 0; box-sizing: border-box; }
  html, body {
    width: 1200px; height: 900px; overflow: hidden;
    background: var(--night);
    font-family: "Old Standard TT", "Century Schoolbook", Georgia, serif;
    color: var(--ink);
  }
  .page { position: relative; width: 1200px; height: 900px; }

  .hero-photo {
    position: absolute; left: 0; top: 0; width: 1200px; height: 730px;
    background:
      radial-gradient(ellipse 300px 240px at 440px 300px, var(--sky-light) 0%, rgba(160,190,195,0.6) 35%, transparent 75%),
      radial-gradient(ellipse 260px 140px at 880px 300px, rgba(200,210,205,0.45) 0%, transparent 80%),
      radial-gradient(ellipse 800px 600px at 520px 360px, var(--sky-mid) 0%, var(--sky-deep) 60%, var(--sky-edge) 100%);
  }

  .masthead {
    position: absolute; left: 0; top: 0; width: 1200px; height: 135px;
    background: var(--header-shade);
  }
  .brand {
    position: absolute; left: 43px; top: 40px;
    font-size: 50px; font-weight: 400; letter-spacing: 0; line-height: 1;
  }
  .masthead-divider {
    position: absolute; left: 335px; top: 28px; width: 1px; height: 77px;
    background: var(--rule);
  }
  .utility-links {
    position: absolute; left: 356px; top: 27px; list-style: none;
    font-size: 14px; letter-spacing: 0.6px; line-height: 26px;
  }

  .main-nav {
    position: absolute; left: 0; top: 135px; width: 1200px; height: 38px;
    background: var(--band); border-top: 1px solid rgba(255,255,255,0.18);
  }
  .main-nav a {
    position: absolute; top: 10px; font-size: 14px; letter-spacing: 0.2px;
    color: var(--ink-muted); text-decoration: none;
  }
  .main-nav a.is-current { color: var(--ink); text-decoration: underline; text-underline-offset: 3px; }

  .hero-title {
    position: absolute; right: 102px; top: 415px;
    font-size: 124px; font-weight: 400; line-height: 1; letter-spacing: 1px;
  }
  .hero-copy {
    position: absolute; left: 340px; top: 526px;
    font-size: 28px; line-height: 36px; letter-spacing: 1.4px;
    white-space: nowrap;
  }

  .site-footer {
    position: absolute; left: 0; top: 730px; width: 1200px; height: 170px;
    background: var(--night);
  }
  .footer-column { position: absolute; top: 14px; }
  .footer-column h3 {
    font-size: 15px; font-weight: 400; letter-spacing: 0.2px; margin-bottom: 9px;
  }
  .footer-column ul { list-style: none; font-size: 14px; line-height: 17px; letter-spacing: 0.2px; color: var(--ink-soft); }
</style>
</head>
<body>
<div class="page">
  <div class="hero-photo" role="img" aria-label="Photograph looking up at a jet airliner crossing a cloudy teal sky beside a street lamp"></div>

  <header class="masthead">
    <div class="brand">VELMIRA</div>
    <div class="masthead-divider"></div>
    <ul class="utility-links">
      <li>MEMBER LOGIN</li>
      <li>JOIN OUR ENTOURAGE</li>
      <li>CONTACT US</li>
    </ul>
  </header>

  <nav class="main-nav">
    <a href="#" style="left:44px">ABOUT US</a>
    <a href="#" style="left:171px">ENTOURAGE &amp; STAFFING</a>
    <a href="#" style="left:409px">EVENTS</a>
    <a href="#" class="is-current" style="left:519px">TRAVEL</a>
    <a href="#" style="left:627px">CELEBRITY &amp; PR</a>
    <a href="#" style="left:801px">OTHER SERVICES</a>
  </nav>

  <h1 class="hero-title">Travel.</h1>
  <p class="hero-copy">A Velmira experience guarantees you insider knowledge,<br>inaccessible products and special rates. Our team will<br>have you arriving stylishly, efficiently, and comfortably<br>for your passport around the world.</p>

  <footer class="site-footer">
    <div class="footer-column" style="left:300px">
      <h3>EVENTS</h3>
      <ul>
        <li>CHARITY &amp; FOUNDATION PARTIES</li>
        <li>FASHION WEEK</li>
        <li>FILM FESTIVAL</li>
        <li>PRIVATE ESTATE EVENTS</li>
        <li>PUBLICATION LAUNCH EVENTS</li>
        <li>ART MERIDIA</li>
      </ul>
    </div>
    <div class="footer-column" style="left:631px">
      <h3>TRAVEL</h3>
      <ul>
        <li>CAR SERVICE</li>
        <li>PRIVATE CHARTER</li>
        <li>YACHTS</li>
        <li>HOTEL</li>
        <li>AIRFARE</li>
      </ul>
    </div>
    <div class="footer-column" style="left:843px">
      <h3>CELEBRITY &amp; PR</h3>
      <ul>
        <li>GRAND OPENINGS</li>
        <li>PRODUCT LAUNCHES</li>
        <li>MUSICIANS</li>
        <li>SPORTS FIGURES</li>
        <li>POLITICIANS</li>
        <li>TOP CHEFS</li>
      </ul>
    </div>
  </footer>
</div>
</body>
</html>
```